Legal Stationary

A full set of stationery is required
The image and logo, along with colour, are set and attached.
The style should be modern, clean, and corporate. Not just a basic template off the web.
In addition to the address/website/email/phone fields for KP and LCB number, with the text “the firm is authorised and regulated by the LCB”
All files in all formats will be needed to allow editing after. Initial setup of templates will be required, and details for 4 business cards will be supplied.
Consumers of legal services
Legal

```html
<!DOCTYPE html>
<html lang="en">
<head>
<meta charset="utf-8">
<title>Calder Law – Stationery Set</title>
<link href="https://fonts.googleapis.com/css2?family=Inter:wght@400;500&display=swap" rel="stylesheet">
<style>
  :root {
    --brand-blue: #25389a;
    --brand-blue-faint: #3347a8;
    --paper: #f6f3f3;
    --paper-white: #ffffff;
    --ink: #222222;
    --ink-soft: #4a4a4a;
    --backdrop: #323334;
    --on-blue: #ffffff;
  }
  * { margin: 0; padding: 0; box-sizing: border-box; }
  html, body { width: 1200px; height: 465px; overflow: hidden; }
  body {
    position: relative;
    background: var(--backdrop);
    font-family: "Inter", Helvetica, Arial, sans-serif;
    color: var(--ink);
  }
  .sheet { position: absolute; background: var(--paper); box-shadow: 0 2px 6px rgba(0,0,0,.45); }
  .wordmark {
    position: absolute;
    font-family: "Inter", Helvetica, Arial, sans-serif;
    font-weight: 500;
    letter-spacing: .02em;
    text-transform: uppercase;
    white-space: nowrap;
    line-height: 1;
    color: var(--brand-blue);
  }
  .tiny { font-size: 4.6px; line-height: 5.8px; color: var(--ink); }
  .icon { width: 4px; height: 4px; display: inline-block; vertical-align: -0.5px; margin-right: 2px; }
  .icon svg { display: block; width: 4px; height: 4px; fill: var(--brand-blue); }

  /* Letterhead */
  .letterhead { left: 31px; top: 40px; width: 279px; height: 393px; }
  .letterhead .wordmark { left: 26px; top: 35px; font-size: 13px; }
  .letterhead .address { position: absolute; right: 80px; top: 33px; text-align: right; }
  .letterhead .divider { position: absolute; left: 204px; top: 32px; width: .5px; height: 19px; background: var(--ink); }
  .letterhead .contacts { position: absolute; left: 208px; top: 33px; }
  .letterhead .salutation { position: absolute; left: 28px; top: 96px; font-size: 7.8px; color: var(--ink-soft); }
  .letterhead .body-copy { position: absolute; left: 28px; top: 119px; width: 225px; }
  .letterhead .body-copy p {
    font-size: 4.4px; line-height: 6.7px; color: var(--ink-soft);
    text-align: justify; margin-bottom: 6.7px;
  }
  .letterhead .sign-off { position: absolute; left: 28px; top: 267px; font-size: 4.6px; color: var(--ink-soft); }
  .letterhead .signature { position: absolute; left: 26px; top: 277px; width: 38px; height: 15px; background: #d9d6d6; border-radius: 2px; }
  .letterhead .signer { position: absolute; left: 29px; top: 298px; font-size: 6.4px; color: var(--ink-soft); }
  .letterhead .signer-role { position: absolute; left: 29px; top: 307px; font-size: 4.8px; color: var(--ink-soft); }
  .regulation { position: absolute; font-size: 4.6px; color: var(--ink); white-space: nowrap; }
  .letterhead .regulation { left: 67px; top: 376px; }

  /* Envelope back */
  .envelope-back { left: 341px; top: 92px; width: 313px; height: 142px; }
  .envelope-back .flap { position: absolute; left: 0; top: 0; width: 313px; height: 53px; }
  .envelope-back .wordmark { left: 0; width: 313px; text-align: center; top: 111px; top: 20px; font-size: 15px; color: var(--on-blue); }

  /* Envelope front */
  .envelope-front { left: 340px; top: 257px; width: 314px; height: 142px; }
  .envelope-front .wordmark { left: 14px; top: 20px; font-size: 13px; }
  .envelope-front .address { position: absolute; left: 14px; top: 43px; }
  .envelope-front .contacts { position: absolute; left: 14px; top: 62px; }
  .envelope-front .regulation { left: 14px; top: 131px; }

  /* Presentation folder */
  .folder { left: 683px; top: 104px; width: 465px; height: 293px; background: var(--paper-white); }
  .folder .back-panel { position: absolute; left: 0; top: 0; width: 232px; height: 293px; background: var(--brand-blue); }
  .folder .back-panel .wordmark { left: 0; width: 232px; text-align: center; top: 132px; font-size: 28px; color: var(--brand-blue-faint); }
  .folder .back-panel .details { position: absolute; left: 0; width: 232px; text-align: center; color: var(--on-blue); font-size: 5.6px; line-height: 7px; }
  .folder .back-panel .address { top: 213px; }
  .folder .back-panel .rule { position: absolute; left: 103px; top: 241px; width: 26px; height: .5px; background: var(--on-blue); }
  .folder .back-panel .contact-list { top: 252px; }
  .folder .front-panel .wordmark { left: 232px; width: 233px; text-align: center; top: 132px; font-size: 28px; }
</style>
</head>
<body>

  <!-- Letterhead -->
  <section class="sheet letterhead" aria-label="Letterhead">
    <div class="wordmark">Calder Law</div>
    <div class="address tiny">2418 Linden Ct<br>200B Elm Ridge<br>IN 46390</div>
    <div class="divider"></div>
    <div class="contacts tiny">
      <div><span class="icon"><svg viewBox="0 0 10 10"><path d="M2 0h2l1 3-1.5 1a6 6 0 0 0 2.5 2.5L7 5l3 1v2a2 2 0 0 1-2 2C4 10 0 6 0 2a2 2 0 0 1 2-2z"/></svg></span>2195550182</div>
      <div><span class="icon"><svg viewBox="0 0 10 10"><path d="M0 2h10v6H0zM0 2l5 3.5L10 2" /></svg></span>info@calderlaw.com</div>
      <div><span class="icon"><svg viewBox="0 0 10 10"><circle cx="5" cy="5" r="5"/></svg></span>www.calderlaw.com</div>
    </div>
    <p class="salutation">Dear Mr. Hale,</p>
    <div class="body-copy">
      <p>Lorem ipsum dolor sit amet, consectetur adipiscing elit. Donec orci purus, luctus vitae dignissim eu, iaculis sed purus. Vivamus faucibus, ipsum nec aliquet viverra, leo mauris condimentum ligula, sit amet sagittis enim ligula quis arcu. Nam egestas tortor id nisi porttitor mattis. In tortor ante, ultricies in suscipit a, tempus non massa. Vivamus et auctor mi. Fusce vel massa nulla. Phasellus nec eros mauris, et scelerisque orci.</p>
      <p>Donec malesuada orci vitae nulla accumsan porta a id massa. Quisque accumsan iaculis magna sit amet fringilla. Maecenas consequat, magna eget tincidunt semper, odio nibh rutrum mi, id feugiat ante nisi eu risus. Vestibulum nunc orci, rhoncus a placerat in, ultricies in mi. Cras mattis varius eros, vel fringilla nisi suscipit eget. Quisque scelerisque sagittis nulla at porttitor.</p>
      <p>Sed id augue vitae urna euismod commodo aliquet a quam. Pellentesque arcu velit, cursus et malesuada ut, consequat et diam. Nullam erat sem, rhoncus id ullamcorper vitae, rhoncus et arcu. In ultricies ultricies nulla, ut rutrum nisi iaculis at. Donec eu magna a metus ornare faucibus. Fusce aliquet faucibus ultricies. Morbi semper, est id tincidunt gravida, sem arcu adipiscing lacus, ac bibendum nulla leo eu purus. Quisque nec diam sed risus consectetur a cumsan quis quis nibh. Vestibulum id purus lorem.</p>
      <p>It is a long established fact that a reader will be distracted by the readable content of a page when looking at its layout. The point of using Lorem Ipsum is that it has a more-or-less normal distribution of letters, as opposed to using 'Content here, content here', making it look like readable English. Many desktop publishing packages</p>
    </div>
    <p class="sign-off">Sincerely,</p>
    <div class="signature" role="img" aria-label="Handwritten signature"></div>
    <p class="signer">Daniel Reeve</p>
    <p class="signer-role">CEO/ Founder</p>
    <p class="regulation">The firm is authorised and regulated by the LCB&nbsp; 412 7780 3195</p>
  </section>

  <!-- Envelope, back with flap -->
  <section class="sheet envelope-back" aria-label="Envelope back">
    <svg class="flap" viewBox="0 0 313 53" preserveAspectRatio="none" aria-hidden="true">
      <path d="M0 0H313L303 35Q298 53 282 53H31Q15 53 10 35Z" fill="var(--brand-blue)"/>
    </svg>
    <div class="wordmark">Calder Law</div>
  </section>

  <!-- Envelope, front -->
  <section class="sheet envelope-front" aria-label="Envelope front">
    <div class="wordmark">Calder Law</div>
    <div class="address tiny">2418 Linden Ct<br>200B Elm Ridge<br>IN 46390</div>
    <div class="contacts tiny">
      <div><span class="icon"><svg viewBox="0 0 10 10"><path d="M2 0h2l1 3-1.5 1a6 6 0 0 0 2.5 2.5L7 5l3 1v2a2 2 0 0 1-2 2C4 10 0 6 0 2a2 2 0 0 1 2-2z"/></svg></span>2195550182</div>
      <div><span class="icon"><svg viewBox="0 0 10 10"><path d="M0 2h10v6H0z"/></svg></span>info@calderlaw.com</div>
      <div><span class="icon"><svg viewBox="0 0 10 10"><circle cx="5" cy="5" r="5"/></svg></span>www.calderlaw.com</div>
    </div>
    <p class="regulation">The firm is authorised and regulated by the LCB&nbsp; 412 7780 3195</p>
  </section>

  <!-- Presentation folder -->
  <section class="sheet folder" aria-label="Presentation folder">
    <div class="back-panel">
      <div class="wordmark">Calder Law</div>
      <p class="details address">2418 Linden Ct<br>200B Elm Ridge<br>IN 46390</p>
      <div class="rule"></div>
      <p class="details contact-list">2195550182<br>info@calderlaw.com<br>www.calderlaw.com</p>
    </div>
    <div class="front-panel">
      <div class="wordmark">Calder Law</div>
    </div>
  </section>

</body>
</html>
```